Business Card Design - Furniture Retail

Open to both Single or double sided design

We are launching a online ecommerce store that sells Scandinavian/Danish style of furniture in Australia.

We aspire to provide stylish but classic and designers' selection of furniture to the Australia public at affordable price. For the style of the furniture we are selling, please see the following links:

https://www.boxlyshare.com/sh/qrk7vz2mwpl04tn/BBXTpeLr3h52Kd7nWqYzRsGmu?dl=0

The style of the design we are looking for is clean, simple that look Scandinavian/Danish but yet it is timeless classic.

Aspiring Design
http://www.hallwick.com
http://brenlowe.com.au/
http://kolvo.furniture/
http://www.tipo.com/
Updates

Please display the card on normal angle for both front and back instead of funny angle. Please keep it display when displaying the design of the business cards so that we can focus on the designs rather than being confused by the unnecessary stuffs like the hands or background

I think there is already enough curve line on the logo itself so anything extra of the curve on the business card would be really unnecessary. Please avoid using any of the extra curve line on the business card, other than the logo itself. Thanks

Regular card and give them a matt celloglaze to create texture on card that makes it looked luxury and expensive.

Please display design on normal angle! Please only use white colour in the background (not the business card but the referring to the submission) rather than anything fancy so that we can focus on the design.

Target Market(s)

High end market consumers who are financially capable and who has good taste and appreciate good design

aged between 28 - 45 white collars professional/businessmen who live in metropolitan areas

Industry/Entity Type

Business

Font styles to use
Serif
Sans Serif

Requirements
Must have
• Regular card and give them a matt celloglaze to create texture on card that makes it looked luxury and expensive.

Please use the logo from the uploaded files

Company Name: Miles Orveda
Name: Peter Holm
Phone: +614 27 505 316
Website: www.milesorveda.com.au
Email: peter@milesorveda.com.au
Nice to have
• Colour is not limited to black and white
Should not have
• The concept photos of the furniture should NOT be used in the FRONT page of the business card.

```html
<!DOCTYPE html>
<html lang="en">
<head>
<meta charset="utf-8">
<title>Miles Orveda — Business Card</title>
<link rel="stylesheet" href="https://fonts.googleapis.com/css2?family=Cinzel:wght@400;600&family=Open+Sans:wght@400&display=swap">
<style>
  :root {
    --page: #ffffff;
    --card-light: #ffffff;
    --card-dark: #0b0f10;
    --ink: #141414;
    --name-ink: #d9d6cc;
    --name-glow: rgba(255, 255, 255, 0.45);
    --contact-ink: #f2f2f2;
    --icon-ink: #cfcfcf;
  }
  * { margin: 0; padding: 0; box-sizing: border-box; }
  html, body {
    width: 1200px;
    height: 900px;
    overflow: hidden;
    background: var(--page);
  }
  .canvas {
    position: relative;
    width: 1200px;
    height: 900px;
  }
  .card {
    position: absolute;
    left: 160px;
    top: 181px;
    width: 880px;
    height: 538px;
    overflow: hidden;
    box-shadow: 0 6px 24px rgba(0, 0, 0, 0.22);
  }
  .card__top {
    position: absolute;
    inset: 0 0 auto 0;
    height: 50%;
    background: var(--card-light);
  }
  .card__bottom {
    position: absolute;
    inset: auto 0 0 0;
    height: 50%;
    background: var(--card-dark);
  }
  .wordmark {
    position: absolute;
    left: 264px;
    top: 126px;
    font-family: "Cinzel", Georgia, serif;
    font-weight: 600;
    font-size: 30px;
    letter-spacing: 1px;
    color: var(--ink);
    white-space: nowrap;
  }
  .holder-name {
    position: absolute;
    left: 519px;
    top: 405px;
    font-family: "Cinzel", Georgia, serif;
    font-weight: 400;
    font-size: 38px;
    letter-spacing: 1px;
    color: var(--name-ink);
    text-shadow: 0 0 6px var(--name-glow), 0 0 12px rgba(255, 255, 255, 0.2);
    white-space: nowrap;
  }
  .contacts {
    position: absolute;
    left: 110px;
    top: 352px;
    list-style: none;
  }
  .contacts__item {
    display: flex;
    align-items: center;
    height: 28px;
    margin-bottom: 25px;
    font-family: "Open Sans", Arial, sans-serif;
    font-size: 16px;
    color: var(--contact-ink);
  }
  .contacts__icon {
    width: 22px;
    height: 22px;
    margin-right: 14px;
    flex: none;
    filter: drop-shadow(0 0 3px rgba(255, 255, 255, 0.35));
  }
</style>
</head>
<body>
<main class="canvas">
  <section class="card" aria-label="Business card">
    <div class="card__top"></div>
    <div class="card__bottom"></div>

    <div class="wordmark">MILES ORVEDA</div>

    <div class="holder-name">Peter Holm</div>

    <ul class="contacts">
      <li class="contacts__item">
        <svg class="contacts__icon" viewBox="0 0 24 24" aria-hidden="true">
          <path fill="var(--icon-ink)" d="M6.6 2.5l3 3.4-1.8 2.3c1 2.4 3.4 5 6 6.2l2.2-1.8 3.5 3-1.6 3.3c-.4.7-1.2 1-2 .8C9.7 18 5.9 14.2 4.1 8.1c-.2-.8.1-1.6.8-2z"/>
        </svg>
        <span>+614 27 505 316</span>
      </li>
      <li class="contacts__item">
        <svg class="contacts__icon" viewBox="0 0 24 24" aria-hidden="true">
          <rect x="2.5" y="5.5" width="19" height="13" fill="none" stroke="var(--icon-ink)" stroke-width="1.8"/>
          <path d="M2.5 5.5l9.5 8 9.5-8M2.5 18.5l7-6.5M21.5 18.5l-7-6.5" fill="none" stroke="var(--icon-ink)" stroke-width="1.6"/>
        </svg>
        <span>peter@milesorveda.com.au</span>
      </li>
      <li class="contacts__item">
        <svg class="contacts__icon" viewBox="0 0 24 24" aria-hidden="true">
          <g fill="none" stroke="var(--icon-ink)" stroke-width="1.5">
            <circle cx="12" cy="12" r="9.5"/>
            <ellipse cx="12" cy="12" rx="4.2" ry="9.5"/>
            <path d="M2.5 12h19M4 7h16M4 17h16M12 2.5v19"/>
          </g>
        </svg>
        <span>www.milesorveda.com.au</span>
      </li>
    </ul>
  </section>
</main>
</body>
</html>
```